Velvet Compass - our client magazine

A quality magazine consisting of a number of bespoke articles in the first half followed by an overview of each company that form part of the group as well as details of the services offered. Vast majority of the copy is attached to provide a good overview of the content required. The magazine will require printing so quality imagery is required.

Industry/Entity Type

Recruitment

Font styles to use
Serif

Colors
0355a3
6b449b
3276b5
876aae
a64599
00a990
5c5c5c
000000
474747

Requirements
Must have
• Bringing the copy to life through flow charts and/or diagrams where possible.

```html
<!DOCTYPE html>
<html lang="en">
<head>
<meta charset="utf-8">
<title>Velvet Compass – Welcome Spread</title>
<link href="https://fonts.googleapis.com/css2?family=Great+Vibes&family=Noticia+Text:wght@400;700&display=swap" rel="stylesheet">
<style>
  :root {
    --backdrop: #e9e7e4;
    --paper: #f7f7f6;
    --purple: #6b449b;
    --magenta: #a64599;
    --lilac: #876aae;
    --ink: #000000;
    --body-ink: #1f1f1f;
    --grey: #5c5c5c;
    --rule: #474747;
  }
  html, body {
    margin: 0;
    width: 1200px;
    height: 1200px;
    overflow: hidden;
    background: var(--backdrop);
  }
  .spread {
    position: absolute;
    left: 40px;
    top: 200px;
    width: 1120px;
    height: 800px;
    background: var(--paper);
    box-shadow: 0 10px 30px rgba(0,0,0,0.18);
  }
  .gutter {
    position: absolute;
    left: 559px;
    top: 0;
    width: 2px;
    height: 800px;
    background: rgba(0,0,0,0.15);
    z-index: 3;
  }
  .feature-photo {
    position: absolute;
    inset: 0;
    z-index: 1;
  }
  .feature-photo svg { display: block; }
  .welcome {
    position: absolute;
    left: 730px;
    top: 50px;
    width: 355px;
    z-index: 2;
    font-family: "Noticia Text", Georgia, serif;
    color: var(--body-ink);
  }
  .welcome-header {
    display: flex;
    align-items: flex-end;
    justify-content: space-between;
    border-bottom: 1px solid var(--rule);
    padding-bottom: 6px;
  }
  .welcome-title {
    font-family: "Great Vibes", cursive;
    font-size: 31px;
    line-height: 1.05;
    margin: 0 0 10px;
    font-weight: 400;
    color: var(--ink);
  }
  .md-portrait {
    width: 118px;
    height: 112px;
    background: linear-gradient(180deg, #d9d8d6 0%, #bfbcb8 60%, #6d6f73 100%);
  }
  .welcome-body {
    font-size: 11.6px;
    line-height: 1.42;
    margin-top: 12px;
  }
  .welcome-body p { margin: 0; }
  .signature {
    font-family: "Great Vibes", cursive;
    font-size: 30px;
    margin: 34px 0 4px;
    color: var(--ink);
  }
  .sign-role {
    font-size: 11.6px;
    line-height: 1.4;
    color: var(--grey);
  }
  .closing-rule {
    margin-top: 30px;
    width: 300px;
    border-top: 1px solid var(--rule);
  }
</style>
</head>
<body>
  <main class="spread">
    <div class="feature-photo" role="img" aria-label="Photograph of a businessman in a suit reading a newspaper beside a café window, with purple tinted overlays">
      <svg width="1120" height="800" viewBox="0 0 1120 800">
        <defs>
          <linearGradient id="photoTone" x1="0" y1="0" x2="0.6" y2="1">
            <stop offset="0" stop-color="#8a6f86"/>
            <stop offset="0.45" stop-color="#5b4b5e"/>
            <stop offset="1" stop-color="#6e2f6a"/>
          </linearGradient>
        </defs>
        <polygon points="0,0 700,0 590,800 0,800" fill="url(#photoTone)"/>
        <polygon points="0,0 420,0 0,470" fill="var(--magenta)" opacity="0.55"/>
        <polygon points="420,0 560,0 230,330" fill="#8f9aa3" opacity="0.45"/>
        <polygon points="0,470 590,800 0,800" fill="var(--purple)" opacity="0.45"/>
        <polygon points="640,0 700,0 680,150 600,150" fill="var(--magenta)" opacity="0.7"/>
        <polygon points="700,0 720,0 700,140 680,150" fill="#111" opacity="0.85"/>
      </svg>
    </div>
    <div class="gutter"></div>

    <article class="welcome">
      <header class="welcome-header">
        <h1 class="welcome-title">Welcome message<br>from MD</h1>
        <div class="md-portrait" role="img" aria-label="Portrait photograph of the managing director"></div>
      </header>
      <div class="welcome-body">
        <p>Hello and welcome to this latest edition of Velvet Compass.</p>
        <p>In this issue, we are considering the importance of “brand” throughout the recruitment process. As Headhunters, our brand and reputation have always been key to our business. It’s important that candidates know and respect us, and that our clients are happy to recommend us to other companies. However, in recent years it has become increasingly important for both clients and candidates to also consider their own brand very carefully.</p>
        <p>With UK unemployment at record low levels, the competition between companies to attract and retain the top talent is getting fiercer all the time. Candidates will often have multiple job options to choose between. The reputation, culture and working environment of each potential employer therefore needs to be carefully researched to ensure the right choice is made. Developing an attractive and effective Employer Brand and Marketing strategy is therefore essential for all companies.</p>
        <p>On the candidate side, brand is equally important when competing for the most attractive roles. This poses some interesting challenges in the modern world. As social media has become an integral part of life today, the separation between our personal and professional lives is being reduced. Candidates need to be aware that their online life is part of their personal brand and can be important for their career.</p>
        <p>We will consider these issues and more over the next few pages. As always, please do not hesitate to contact us with any questions or comments which arise.</p>
        <p>I hope you enjoy reading ............ and look forward to working with you soon.</p>
        <p>Sincerely,</p>
      </div>
      <div class="signature">Martin Hale</div>
      <div class="sign-role">Co-Founder &amp; CEO<br>The Northvale Group</div>
      <div class="closing-rule"></div>
    </article>
  </main>
</body>
</html>
```